Software - upgrade look and feel

Brightwell Tallyworks is the worldwide distributor of the zLumio software application, which powers a loan strategy as described at www.brightwelltallyworks.com.The company has recently upgraded its image and website; and now seeks to give zLumio a much-needed face-lift.Using the screen shots of the existing application (2 x screens provided), recreate the screens in a modern and vibrant style that generates a feeling of professionalism and confidence.

Target Market(s)

Financial services industry and their clients.

Industry/Entity Type

Financial Service

Font styles to use
Other font styles liked:
• See our website at brightwelltallyworks.com - happy with this font, but open to ideas.

Colors

Designer to choose colors to be used in the design.

Requirements
Must have
• Existing fields, but perhaps more intuitive for the User.
Nice to have
• A less busy look that suggests an innovative software application.
Should not have
• Complication.

```html
<!DOCTYPE html>
<html lang="en">
<head>
<meta charset="utf-8">
<title>zLumio – Client / Income</title>
<link href="https://fonts.googleapis.com/css2?family=Fira+Sans:ital,wght@0,400;0,500;0,600;1,400&display=swap" rel="stylesheet">
<style>
  :root {
    --bg: #555965;
    --nav-active: #434651;
    --field: #23252f;
    --teal: #1fc2ad;
    --teal-dark: #19a897;
    --text: #ffffff;
    --muted: #e6e8ee;
    --avatar-a: #c7a48f;
    --avatar-b: #7b5a4a;
  }
  * { box-sizing: border-box; margin: 0; padding: 0; }
  html, body { width: 1200px; height: 912px; overflow: hidden; }
  body {
    position: relative;
    background: var(--bg);
    font-family: "Fira Sans", Arial, sans-serif;
    color: var(--text);
  }
  .abs { position: absolute; }

  /* Sidebar */
  .brand { left: 51px; top: 22px; height: 26px; line-height: 26px; }
  .brand-name { font-size: 19px; font-weight: 600; }
  .nav { left: 0; top: 84px; width: 196px; list-style: none; }
  .nav-item {
    height: 42px; display: flex; align-items: center; gap: 12px;
    padding-left: 19px; font-size: 14.5px; margin-bottom: 8px;
  }
  .nav-item svg { width: 18px; height: 18px; fill: none; stroke: var(--teal); stroke-width: 1.8; stroke-linecap: round; stroke-linejoin: round; }
  .nav-item.active { background: var(--nav-active); border-right: 3px solid var(--teal); }

  /* Headings & labels */
  .section-title { left: 235px; font-size: 16px; font-weight: 600; }
  .label { font-size: 14px; line-height: 31px; height: 31px; }
  .label-stack { font-size: 14px; line-height: 17px; }
  .label-stack small { display: block; font-size: 10px; font-style: italic; color: var(--muted); }

  /* Fields */
  .field {
    height: 31px; border-radius: 16px; background: var(--field);
    font-size: 13px; line-height: 31px; padding-left: 16px; color: var(--text);
  }
  .field .chev { position: absolute; right: 17px; top: 12px; width: 10px; height: 7px; fill: none; stroke: var(--teal); stroke-width: 2; }
  .left-field { left: 327px; width: 317px; }
  .right-field { left: 834px; width: 316px; }
  .sim-field { left: 337px; width: 315px; }
  .freq-field { left: 675px; width: 315px; }

  .client-pill {
    left: 327px; width: 175px; height: 30px; border-radius: 15px; background: var(--field);
    display: flex; align-items: center; gap: 9px; padding-left: 2px; font-size: 12px;
  }
  .avatar { width: 28px; height: 28px; border-radius: 50%; border: 2px solid #fff; flex: none; }
  .avatar.a { background: linear-gradient(135deg, var(--avatar-a), #8a6a5c); }
  .avatar.b { background: linear-gradient(135deg, var(--avatar-b), #3a2c28); }

  /* More options */
  .more-btn {
    left: 1012px; width: 138px; height: 33px; border-radius: 17px; background: var(--teal);
    font-size: 12.5px; line-height: 33px; padding-left: 13px;
  }
  .more-btn svg { position: absolute; right: 14px; top: 13px; width: 10px; height: 7px; fill: none; stroke: #fff; stroke-width: 2; }
  .menu {
    left: 965px; width: 185px; background: var(--teal); border-radius: 4px;
    list-style: none; z-index: 2; box-shadow: 0 4px 10px rgba(0,0,0,.18);
  }
  .menu li { height: 35px; line-height: 35px; padding-left: 10px; font-size: 12.5px; border-bottom: 1px solid var(--teal-dark); }
  .menu li:last-child { border-bottom: none; }

  .instruction { left: 235px; top: 497px; font-size: 10.5px; font-weight: 600; line-height: 15px; }
  .col-head { top: 544px; font-size: 10px; font-style: italic; }
  .note { left: 235px; top: 698px; font-size: 10px; font-style: italic; line-height: 12px; }
  .footnote { left: 702px; top: 843px; font-size: 10px; font-style: italic; }

  .btn {
    top: 833px; width: 103px; height: 33px; border-radius: 17px;
    font-size: 12.5px; font-weight: 600; text-align: center; line-height: 31px; letter-spacing: .5px;
  }
  .btn-save { left: 928px; background: var(--teal); border: 1px solid var(--teal); }
  .btn-cancel { left: 1047px; border: 1px solid var(--teal); color: var(--teal); }
</style>
</head>
<body>

  <div class="abs brand"><span class="brand-name">zLumio</span></div>

  <ul class="abs nav">
    <li class="nav-item active"><svg viewBox="0 0 18 18"><circle cx="9" cy="5.5" r="3.5"/><path d="M2.5 17c0-4 3-6 6.5-6s6.5 2 6.5 6"/></svg>Client / Income</li>
    <li class="nav-item"><svg viewBox="0 0 18 18"><path d="M1.5 13l5-5 3.5 3.5 6-6"/><path d="M12 5.5h4v4"/></svg>Expneses</li>
    <li class="nav-item"><svg viewBox="0 0 18 18"><rect x="2" y="5.5" width="14" height="10" rx="1.5"/><path d="M6.5 5.5V3h5v2.5M9 5.5v10"/></svg>Assets / Liablities</li>
    <li class="nav-item"><svg viewBox="0 0 18 18"><path d="M2 4.5h14M2 9h14M2 13.5h14"/><circle cx="6" cy="4.5" r="1.5"/><circle cx="12" cy="9" r="1.5"/><circle cx="7" cy="13.5" r="1.5"/></svg>Restructure</li>
    <li class="nav-item"><svg viewBox="0 0 18 18"><path d="M8 2.5a6.5 6.5 0 1 0 7.5 7.5H8z"/><path d="M10.5 1.5a6 6 0 0 1 6 6h-6z"/></svg>Calculate</li>
  </ul>

  <!-- General information -->
  <h2 class="abs section-title" style="top:32px">General Information</h2>

  <span class="abs label" style="left:235px;top:72px">Client:</span>
  <div class="abs client-pill" style="top:72px"><span class="avatar a" role="img" aria-label="Client photo"></span>Owen Darrow</div>
  <div class="abs client-pill" style="top:110px"><span class="avatar b" role="img" aria-label="Client photo"></span>Mira Darrow</div>

  <div class="abs more-btn" style="top:72px">More Options<svg viewBox="0 0 10 7"><path d="M1 6l4-4 4 4"/></svg></div>
  <ul class="abs menu" style="top:111px">
    <li>Additional Info</li><li>Statistics</li><li>Send to Pending tray</li>
  </ul>

  <span class="abs label" style="left:235px;top:152px">File No.</span>
  <div class="abs field left-field" style="top:152px">1234-998629-901</div>
  <span class="abs label" style="left:235px;top:198px">View</span>
  <div class="abs field left-field" style="top:198px">Client 1<svg class="chev" viewBox="0 0 10 7"><path d="M1 1l4 4 4-4"/></svg></div>
  <span class="abs label" style="left:235px;top:244px">Loan Writer</span>
  <div class="abs field left-field" style="top:244px">Halvers, Dean (123-4567890)<svg class="chev" viewBox="0 0 10 7"><path d="M1 1l4 4 4-4"/></svg></div>
  <span class="abs label" style="left:235px;top:291px">CS Officer</span>
  <div class="abs field left-field" style="top:291px">Halvers, Dean (123-4567890)<svg class="chev" viewBox="0 0 10 7"><path d="M1 1l4 4 4-4"/></svg></div>

  <span class="abs label" style="left:731px;top:152px">Title</span>
  <div class="abs field right-field" style="top:152px">Client Title</div>
  <span class="abs label" style="left:731px;top:198px">Family Name</span>
  <div class="abs field right-field" style="top:198px">Darrow</div>
  <span class="abs label" style="left:731px;top:244px">First Name</span>
  <div class="abs field right-field" style="top:244px">Owen<svg class="chev" viewBox="0 0 10 7"><path d="M1 1l4 4 4-4"/></svg></div>
  <span class="abs label" style="left:731px;top:291px">Email</span>
  <div class="abs field right-field" style="top:291px">owenmira@mailhollow.com</div>

  <!-- Simulation purpose -->
  <h2 class="abs section-title" style="top:374px">Simulation Purpose</h2>

  <span class="abs label" style="left:235px;top:413px">Strategy</span>
  <div class="abs field sim-field" style="top:413px">Strategy 1<svg class="chev" viewBox="0 0 10 7"><path d="M1 1l4 4 4-4"/></svg></div>

  <div class="abs more-btn" style="top:410px">More Options<svg viewBox="0 0 10 7"><path d="M1 6l4-4 4 4"/></svg></div>
  <ul class="abs menu" style="top:450px">
    <li>Minimisation Strategy</li><li>NLFA Guidelines</li>
  </ul>

  <p class="abs instruction">Please Enter the Names of Client 1 and Client 2 (if Applicable), then Enter<br>after tax wag or salary per frequency of payments.</p>

  <span class="abs col-head" style="left:321px">Net (After Tax)</span>
  <span class="abs col-head" style="left:675px">Frequency of payment</span>

  <span class="abs label" style="left:235px;top:568px">Client 1</span>
  <div class="abs field sim-field" style="top:568px">$ 1,000.00</div>
  <div class="abs field freq-field" style="top:568px">Weekly<svg class="chev" viewBox="0 0 10 7"><path d="M1 1l4 4 4-4"/></svg></div>

  <span class="abs label" style="left:235px;top:615px">Client 2</span>
  <div class="abs field sim-field" style="top:615px">$ 1,500.00</div>
  <div class="abs field freq-field" style="top:615px">Fortnightly<svg class="chev" viewBox="0 0 10 7"><path d="M1 1l4 4 4-4"/></svg></div>

  <p class="abs note">Note: Unless You enter the name of Client 1, no income<br>will be saved for Client 1. Same goes for the Client 2!</p>

  <div class="abs label-stack" style="left:235px;top:743px">Client 1<small>After Tax income</small></div>
  <div class="abs field sim-field" style="top:743px">$ 52,000.00</div>
  <div class="abs label-stack" style="left:731px;top:743px">Combined<small>After Tax income</small></div>
  <div class="abs field right-field" style="top:743px">$ 91,500.00</div>

  <span class="abs footnote">Totals are updated by clicking "Save"</span>
  <div class="abs btn btn-save">SAVE</div>
  <div class="abs btn btn-cancel">CANCEL</div>

</body>
</html>
```